Crema Nook Business card design

i would like a 2 sided business card made please that uses the company logo and address and number details on one side. On the other side i would like to have a buy 4 get one free coffee voucher that we can cross or stamp off every time the customer comes.

Target Market(s)

Target market is for our coffee customers

Industry/Entity Type

Business

Contact Information for Business Card

address: 41 harbourline Cairns city
Phone: 0748296137

Colors
abd036
9bcb3b
ffffff

```html
<!DOCTYPE html>
<html lang="en">
<head>
<meta charset="utf-8">
<title>Crema Nook – Business Card</title>
<link href="https://fonts.googleapis.com/css2?family=Jost:wght@400;500;600;700&display=swap" rel="stylesheet">
<style>
  :root {
    --backdrop: #d8d8d8;
    --card: #ffffff;
    --card-shade: #ececec;
    --green: #8dc340;
    --green-light: #9bcb3b;
    --brown: #4a2c1d;
    --white: #ffffff;
  }
  * { margin: 0; padding: 0; box-sizing: border-box; }
  html, body {
    width: 1200px; height: 1000px; overflow: hidden;
    background: var(--backdrop);
    font-family: "Jost", "Futura", sans-serif;
  }
  .card {
    position: absolute; left: 333px; width: 535px; height: 305px;
    background: linear-gradient(160deg, var(--card) 0%, #f7f7f7 45%, var(--card-shade) 70%, var(--card) 100%);
    box-shadow: 0 1px 3px rgba(0,0,0,0.12);
    overflow: hidden;
  }
  .card--front { top: 183px; }
  .card--back { top: 511px; }

  .brand {
    position: absolute; text-align: center; color: var(--brown);
  }
  .card--front .brand { left: 0; right: 0; top: 238px; }
  .card--back .brand { left: 14px; width: 150px; top: 598px; }
  .brand__name {
    font-weight: 600; font-size: 34px; letter-spacing: 1px; line-height: 1;
    color: var(--brown);
  }
  .card--back .brand__name { font-size: 26px; }
  .brand__rule {
    height: 2px; background: var(--brown); margin: 14px auto 10px; width: 180px;
  }
  .card--back .brand__rule { width: 148px; margin: 12px auto 8px; }
  .brand__roaster {
    font-weight: 700; font-size: 18px; letter-spacing: 2px; line-height: 1;
  }
  .card--back .brand__roaster { font-size: 14px; }
  .brand__tagline {
    font-weight: 600; font-size: 6.5px; letter-spacing: 0.4px; margin-top: 4px;
  }
  .card--back .brand__tagline { font-size: 5.5px; }

  .contact-band {
    position: absolute; left: 0; right: 0; bottom: 0; height: 59px;
    background: var(--green);
    color: var(--white); font-size: 13px; line-height: 18px;
    padding: 9px 0 0 308px;
  }

  .voucher { position: absolute; left: 201px; top: 78px; }
  .voucher__title {
    color: var(--brown); font-size: 19px; font-weight: 400; line-height: 1;
  }
  .stamp-row { display: flex; margin-top: 9px; }
  .stamp {
    width: 75px; height: 85px; border: 1px solid var(--green-light);
    margin-left: -1px; display: flex; align-items: center; justify-content: center;
  }
  .stamp:first-child { margin-left: 0; }
  .stamp svg { width: 32px; height: 28px; }
</style>
</head>
<body>

<section class="card card--front">
  <div class="brand" style="top:55px">
    <div class="brand__name">Crema Nook</div>
    <div class="brand__rule"></div>
    <div class="brand__roaster">Kettleby</div>
    <div class="brand__tagline">SPECIALTY COFFEE ROASTERS</div>
  </div>
  <div class="contact-band">
    <p class="contact-band__address">Address: 41 harbourline Cairns city</p>
    <p class="contact-band__phone">Phone: 0748296137</p>
  </div>
</section>

<section class="card card--back">
  <div class="brand" style="top:87px">
    <div class="brand__name">Crema Nook</div>
    <div class="brand__rule"></div>
    <div class="brand__roaster">Kettleby</div>
    <div class="brand__tagline">SPECIALTY COFFEE ROASTERS</div>
  </div>
  <div class="voucher">
    <h2 class="voucher__title">buy 4 get one free coffee</h2>
    <div class="stamp-row">
      <div class="stamp"><svg viewBox="0 0 32 28" aria-hidden="true"><path d="M13 2c-2 2 2 3 0 6M17 2c-2 2 2 3 0 6" stroke="#8dc340" stroke-width="1.3" fill="none"/><path d="M4 12h20v3c0 5-4 8-10 8s-10-3-10-8z" fill="#8dc340"/><path d="M24 14h2a3 3 0 0 1 0 6h-3" stroke="#8dc340" stroke-width="2" fill="none"/><rect x="2" y="24" width="24" height="2" rx="1" fill="#8dc340"/></svg></div>
      <div class="stamp"><svg viewBox="0 0 32 28" aria-hidden="true"><path d="M13 2c-2 2 2 3 0 6M17 2c-2 2 2 3 0 6" stroke="#8dc340" stroke-width="1.3" fill="none"/><path d="M4 12h20v3c0 5-4 8-10 8s-10-3-10-8z" fill="#8dc340"/><path d="M24 14h2a3 3 0 0 1 0 6h-3" stroke="#8dc340" stroke-width="2" fill="none"/><rect x="2" y="24" width="24" height="2" rx="1" fill="#8dc340"/></svg></div>
      <div class="stamp"><svg viewBox="0 0 32 28" aria-hidden="true"><path d="M13 2c-2 2 2 3 0 6M17 2c-2 2 2 3 0 6" stroke="#8dc340" stroke-width="1.3" fill="none"/><path d="M4 12h20v3c0 5-4 8-10 8s-10-3-10-8z" fill="#8dc340"/><path d="M24 14h2a3 3 0 0 1 0 6h-3" stroke="#8dc340" stroke-width="2" fill="none"/><rect x="2" y="24" width="24" height="2" rx="1" fill="#8dc340"/></svg></div>
      <div class="stamp"><svg viewBox="0 0 32 28" aria-hidden="true"><path d="M13 2c-2 2 2 3 0 6M17 2c-2 2 2 3 0 6" stroke="#8dc340" stroke-width="1.3" fill="none"/><path d="M4 12h20v3c0 5-4 8-10 8s-10-3-10-8z" fill="#8dc340"/><path d="M24 14h2a3 3 0 0 1 0 6h-3" stroke="#8dc340" stroke-width="2" fill="none"/><rect x="2" y="24" width="24" height="2" rx="1" fill="#8dc340"/></svg></div>
    </div>
  </div>
</section>

</body>
</html>
```